KREPvalMusic & KREPvalGuitarLessons Website
Music teaching.
KREPvalMusic & KREPvalGuitarLessons Website - Music
Creative Brief
Music
www.krepvalmusic.example
KREP Val Music is a company that will house 5 different businesses
1) KREP Val Online Music Lessons
2) KREP Val Publishing (for my 2 books)
3) KREP Val Recording
4) KREP Val Production
5) KREP Val Guitar Lessons.
Each of these will have a separate website, I have all the domain names already registered. Each website will look and feel the same, only the website name will differ for each individual business.
Here's some trivia that might be inspiring:
KREP (has many different meaning in Flemish and Dutch): it means anywhere from "Being in Love", to also meaning "unconventional", "crazy" (in any possible form and meaning of that word), but also "mentally unstable", "impressive", etc...
Val: different meanings as well... "Meaning" (as in for example "meaning of life", it also means "sentence" (as in sentences in a language), it also means "lust" (ohh yeahhh haha), "liking", "setting your mind to something", etc...
In combination, the word "Val" in Flemish means "to be"... so literally translated as whole, from Flemish... this would mean" "To Be Crazy".
My main reason for this business name, when I brainstormed this because I needed one, was that it stands out and is memorable with the 2 Z's
AND
It was important to me that the words would be short enough so English speaking people would pronounce the words EXACTLY as they are pronounced in Flemish and Dutch... which is the case. Yaaaay.
Message my company and my website wants to convey:
1) "Fun" is serious business fpr KREP Val Music.
2) KREP Val Music rocks your world.
3) We are creative and inventive
4) YOU are important to us (the bigger head/globe creates that impression strongly)
5) You can "belt" out with us without and be yourself and we help you find your voice.
6) We work focused and structured, but are not rigid. (the falling letters at the end of the logo, being support by the word "music")... we have a plan and direction, and vision, but easily adapt our approach to your needs. I think the design manages to evoke that pretty well... it looks playful but has some sense of balance and structure in it as well.
7) We are fun to work with, flexible and we get things done
This post is for the creation of the guitar lessons website www.KREPvalGuitarLessons.example
"KREP Val Guitar Lessons" offers personalized private guitar instruction incorporating principles of super-study, psychology, music pedagogy, time management & neuroscience
I like the idea of having the tagline/sales line...
"From Fretfumble to Fretfame"
underneath the logo.
I LOVE everything about Quince and I also love their website. It has a cool feeling of space, design, and nice graphics. I want my site to have the same sophisticated, clean, fresh, clear, open feel like the Quince website. I want black text on white background. I want the whole website to be entirely visible without needing to scroll. I would dislike my website looking too much like a template or Pagesmith template. I want it to look like it's custom designed. I want following links/navigation: 1) home I probably would provide the same info like this guy http://www.strumschoolbay.example/faq.htm 2) About Lorsa 3) The Lessons 4) Tuition 5) Testimonials 6) Support 7) FAQ 8) Gallery. Then there is info I want on every page. 1) Contact info. (as on http://www.strumschoolbay.example/faq.htm) Following 7 things that I want on every page, I would like this info like on the Quince website, in cool little link boxes at the bottom of each page, that you click on and a new page then opens up from there. ( I have attached/uploaded a picture called "link boxes), which I took from the quince website to showcase what I mean. I want to have a cool, glossy, sophisticated graphic in every link box/button, just like on the quince website) 2) A box for a student testimonial on top of every page: 3) a Free Resources box: This would be a newsletter, in the form of a little content box showing up on every page with a link. (Which will lead to an info page) (as in http://doratelvik.example/resources/) 4) a box/button that says: "What’s Your Sticking Point?" 5) A 30 second Video Tips. box 6) a Social Networking box. This would be a box that holds links (as icons) where students can further connect to me on my Chatterly, Peepline, Vidcove etc page. 7) A “Buy Now” link/button or box with a link to CoinPost on EVERY page (besides obviously the tuition page) so visitors can buy their lessons from any page). 8) Subscribe boxes: (which would be linked to different email campaigns ). 9) a box labeled "The Challenge" I like having all my contact info in the header, like here http://www.strumschoolbay.example/index.html But I dislike headers that big... I want my header to take up little space on the page, like here http://www.quince.example/ (but maybe a tad bigger than this, as my logo will have to fit in the header)
White
Blue Greenish color as in my logo
Silverish
below header
http://www.quince.example/
http://www.strumschoolbay.example/index.html
http://doratelvik.example/
I want the site to have a glossy, sophisticated look, but every organized, structured and easy to navigate.

```html
<!DOCTYPE html>
<html lang="en">
<head>
<meta charset="utf-8">
<title>KREPval Guitar Lessons</title>
<link rel="stylesheet" href="https://fonts.googleapis.com/css2?family=Open+Sans:wght@400;600;700&family=Cinzel:wght@400;700&family=Marcellus&display=swap">
<style>
:root{
  --teal:#1aa7b8;
  --teal-dark:#0f7f8e;
  --ink:#222;
  --grey:#666;
  --silver:#e4e6e8;
  --silver-dark:#c9cdd1;
  --nav-top:#4a4d51;
  --nav-bottom:#1c1e20;
  --page:#ffffff;
  --gold:#b9893f;
}
*{margin:0;padding:0;box-sizing:border-box}
html,body{width:1200px;height:857px;overflow:hidden;background:var(--page)}
body{position:relative;font-family:"Open Sans",Arial,sans-serif;color:var(--ink)}
.abs{position:absolute}

/* header */
.brand{left:158px;top:34px;display:flex;align-items:center;gap:12px}
.brand-dot{width:40px;height:40px;border-radius:50%;background:var(--teal)}
.brand-name{font-size:24px;font-weight:600;color:var(--ink);line-height:28px}
.tagline{left:430px;top:30px;font-family:"Cinzel",serif;font-size:26px;line-height:32px;color:#3a3d40;letter-spacing:1px}
.contact{left:790px;top:24px;display:flex;gap:12px}
.contact-lines{font-size:14px;color:var(--grey);line-height:18px}
.contact-lines .cta{color:var(--teal);font-weight:600}
.contact-lines .phone{font-size:28px;color:#1b1d1f;line-height:36px;font-weight:600}

/* nav */
.nav{left:156px;top:108px;width:900px;height:36px;border-radius:4px;background:linear-gradient(var(--nav-top),var(--nav-bottom));display:flex}
.nav a{color:#fff;text-decoration:none;font-size:15px;font-weight:700;line-height:36px;padding:0 24px;border-right:1px solid #555}
.nav a.active{background:linear-gradient(#2dc0d0,var(--teal-dark));border-radius:4px 0 0 4px}

/* hero */
.hero{left:156px;top:156px;width:900px;height:380px;border:1px solid var(--silver-dark);background:linear-gradient(#f7f8f9,#e9ebed)}
.hero-art{left:16px;top:10px;width:496px;height:358px;background:radial-gradient(ellipse at 45% 50%,#ffffff,#d6d9dc 70%);border-radius:6px}
.hero-panel{left:524px;top:16px;width:362px;height:350px}
.hero-title{font-family:"Marcellus",serif;font-weight:400;font-size:19px;line-height:25px;color:#55595d}
.hero-title em{font-style:normal;color:var(--teal)}
.hero-text{margin-top:14px;font-size:12px;line-height:17px;color:#444;background:rgba(255,255,255,.6);padding:10px 12px 4px;border-top:1px solid var(--silver-dark)}
.hero-text p{margin-bottom:8px}
.hero-more{text-align:right;font-family:"Marcellus",serif;color:var(--gold);font-size:16px;margin-top:6px}
.arrow{width:28px;height:32px;top:320px}

/* boxes */
.box{top:547px;height:173px;border:1px solid var(--silver-dark);border-radius:4px;background:linear-gradient(#fff,#eef0f2)}
.box h3{font-size:15px;font-weight:700;color:#fff;background:linear-gradient(var(--nav-top),var(--nav-bottom));padding:6px 10px;border-radius:4px 4px 0 0}
.box p{font-size:12.5px;line-height:17px;color:#555;padding:10px 10px 0}
.box .sig{color:var(--teal);font-size:12px;padding-top:6px}
.btn{position:absolute;bottom:12px;left:56px;background:#222;color:#fff;font-size:11px;font-weight:700;padding:4px 18px;border-radius:10px}
.ph{position:absolute;border-radius:6px}
.sub-label{color:var(--teal);font-weight:600;font-size:13px;padding:4px 10px 0}
.email-field{margin:30px 10px 0;height:26px;border:1px solid #bbb;background:#fff;font-size:12px;color:#999;padding:4px 8px}

/* strip */
.strip{top:732px;height:60px;border:1px solid var(--silver-dark);border-radius:4px;background:linear-gradient(#fff,#eceef0);display:flex;align-items:center;gap:10px;padding:0 12px}
.strip .lead{font-size:14px;font-weight:700;color:#444;line-height:18px}
.strip .lead span{color:var(--teal)}
.mark{font-size:22px;font-weight:700;color:var(--teal-dark)}
.social{font-size:11px;font-weight:600;color:#fff;display:flex;gap:6px}
.social span{background:var(--teal-dark);padding:6px 5px;border-radius:3px}

/* footer */
.foot-links{left:156px;top:812px;font-size:12px;color:#1f5f9e}
.foot-copy{right:144px;top:812px;font-size:12px;color:#777}
.wave{left:0;top:828px}
</style>
</head>
<body>

<header>
  <div class="abs brand">
    <div class="brand-dot"></div>
    <div class="brand-name">KREPval<br>Guitar Lessons</div>
  </div>
  <div class="abs tagline">FROM FRETFUMBLE<br>TO FRETFAME</div>
  <div class="abs contact">
    <svg width="34" height="50" viewBox="0 0 38 52"><rect x="4" y="2" width="30" height="48" rx="5" fill="#222"/><rect x="8" y="8" width="22" height="30" fill="#6a6e72"/><circle cx="19" cy="44" r="3" fill="#999"/></svg>
    <div class="contact-lines">
      <div class="cta">Get Started! Contact Us Today</div>
      <div class="phone">1.(555).204.7731</div>
      <div>info@krepvalmusic.example</div>
    </div>
  </div>
</header>

<nav class="abs nav">
  <a class="active">About Lorsa</a><a>The Lessons</a><a>Tuition</a><a>Testimonials</a><a>Support</a><a>FAQ</a><a>Gallery</a>
</nav>

<section class="abs hero">
  <div class="abs hero-art" role="img" aria-label="Guitar neck with strings and faint music notes"></div>
  <div class="abs hero-panel">
    <h1 class="hero-title">WE ARE FUN TO <em>WORK</em> WITH,<br><em>FLEXIBLE</em> AND WE GET THINGS DONE</h1>
    <div class="hero-text">
      <p>KREP means anywhere from "Being in Love", to "unconventional", "crazy" (in any possible meaning of that word), but also "impressive" or out there.</p>
      <p>Val in Dutch means "Meaning" (as in for example: "the meaning of life"). It also means "sentence" (as in: a series of words), but also "lust" or "liking".</p>
      <p>In combination with KREP, the word "Val" in Flemish, means "to be".</p>
      <p>This site is for those who tend "To Be Crazy"</p>
    </div>
    <div class="hero-more">ABOUT MUSIC.</div>
  </div>
</section>
<svg class="abs arrow" style="left:142px" viewBox="0 0 28 32"><rect width="28" height="32" rx="3" fill="#2a2c2e"/><path d="M18 9 L9 16 L18 23Z" fill="#fff"/></svg>
<svg class="abs arrow" style="left:1034px" viewBox="0 0 28 32"><rect width="28" height="32" rx="3" fill="#2a2c2e"/><path d="M10 9 L19 16 L10 23Z" fill="#fff"/></svg>

<section class="abs box" style="left:156px;width:216px">
  <h3>TESTIMONIALS</h3>
  <p style="width:120px">Lorem Ipsum is simply dummy text of the printing.</p>
  <p class="sig">Writer's Name</p>
  <div class="ph" style="left:130px;top:44px;width:72px;height:62px;background:linear-gradient(#5fb6e6,#1f6fb0)" role="img" aria-label="Glossy speech bubble icon"></div>
  <span class="btn">READ MORE</span>
</section>
<section class="abs box" style="left:377px;width:216px">
  <h3>FREE RESOURCES</h3>
  <p style="width:120px">Lorem ipsum dolor sit amet, consectetur adipisicing elit, sed do eiusmod.</p>
  <div class="ph" style="left:130px;top:44px;width:74px;height:70px;background:linear-gradient(#d94a3c,#3a3a3a)" role="img" aria-label="Headphones on a book icon"></div>
  <span class="btn">READ MORE</span>
</section>
<section class="abs box" style="left:600px;width:216px">
  <h3>VIDEO TIPS</h3>
  <div class="ph" style="left:10px;top:40px;width:194px;height:120px;background:linear-gradient(#a08466,#3d3128);border-radius:2px" role="img" aria-label="Video still of a guitar lesson"></div>
  <svg class="abs" style="left:88px;top:86px" width="38" height="28" viewBox="0 0 38 28"><rect width="38" height="28" rx="5" fill="#fff" opacity=".85"/><path d="M15 8 L25 14 L15 20Z" fill="#222"/></svg>
</section>
<section class="abs box" style="left:828px;width:228px">
  <h3>SUBSCRIBE NEWSLETTER</h3>
  <div class="sub-label">to the KREPval.example</div>
  <div class="email-field">Enter Email Address...</div>
  <span class="btn" style="left:64px">SUBSCRIBE</span>
</section>

<section class="abs strip" style="left:156px;width:216px">
  <div class="lead">WHAT'S YOUR<br><span>STICKING POINT?</span></div>
  <svg width="40" height="40" viewBox="0 0 40 40"><path d="M20 3 L25 15 L38 15 L27 23 L31 36 L20 28 L9 36 L13 23 L2 15 L15 15Z" fill="var(--teal)"/></svg>
</section>
<section class="abs strip" style="left:377px;width:216px">
  <div class="lead">THE CHALLENGE<br><span>Are you up for it?</span></div>
  <svg width="36" height="40" viewBox="0 0 36 40"><path d="M8 4 H28 V14 A10 10 0 0 1 8 14Z" fill="var(--teal)"/><rect x="16" y="24" width="4" height="8" fill="var(--teal-dark)"/><rect x="10" y="32" width="16" height="5" fill="var(--teal-dark)"/></svg>
</section>
<section class="abs strip" style="left:600px;width:216px">
  <div class="lead" style="font-size:17px">BUY NOW</div>
  <div class="mark">CoinPost</div>
</section>
<section class="abs strip" style="left:828px;width:228px;padding:0 8px">
  <div class="social"><span>Chatterly</span><span>Peepline</span><span>Vidcove</span><span>Feed</span></div>
</section>

<footer>
  <div class="abs foot-links">About Lorsa &nbsp;|&nbsp; Sitemap &nbsp;|&nbsp; FAQ &nbsp;|&nbsp; Support &nbsp;|&nbsp; Contacts</div>
  <div class="abs foot-copy">© 2011. KREPval.example. All rights reserved</div>
  <svg class="abs wave" width="1200" height="29" viewBox="0 0 1200 29"><path d="M0 29 Q600 -6 1200 29Z" fill="var(--teal)" opacity=".85"/></svg>
</footer>

</body>
</html>
```